Company Website for an IT business called "BRIGHT HARBOR"

Complete website creation with text and graphics.
We need :
- modern and creative design for our IT company
- Content management system to edit text later on
- Integrate third party content from partner company
- Contact form (transfer by email)
Updates

Target Market(s)

Small and medium business
private customers

Industry/Entity Type

Information Technology

Coding

Coded - Design and coding required

Number of Pages Required

1 page

Font styles to use
Sans Serif

Requirements
Must have
• Contact form
Link to legal information
Link to data protection (GDPR)
Link to website owner declaration
Nice to have
• Fresh and creative graphics for IT business

```html
<!DOCTYPE html>
<html lang="en">
<head>
<meta charset="utf-8">
<title>Bright Harbor – IT Services</title>
<link href="https://fonts.googleapis.com/css2?family=Roboto:wght@400;500;700;900&display=swap" rel="stylesheet">
<style>
:root{
  --blue:#1a8fd6;
  --blue-dark:#0f6fb0;
  --ink:#141414;
  --text:#5d6470;
  --soft:#f1f7fd;
  --card:#f4f8fc;
  --line:#e3e9f0;
  --black:#050505;
  --white:#ffffff;
}
*{box-sizing:border-box;margin:0;padding:0}
html,body{width:1200px;height:4785px;overflow:hidden}
body{font-family:"Roboto",Arial,sans-serif;color:var(--ink);background:var(--white);position:relative}
.abs{position:absolute}
.btn{position:absolute;display:flex;align-items:center;justify-content:center;background:var(--blue);color:var(--white);font-weight:700;font-size:16px;letter-spacing:.5px;border-radius:28px}
.photo{position:absolute}
.mark{display:inline-block;width:26px;height:26px;border:3px solid var(--blue)}

/* hero */
.hero{position:absolute;left:0;top:0;width:1200px;height:607px;background:linear-gradient(100deg,#f4f6f8 0%,#e4e9ee 40%,#b9c4cc 70%,#8e9ba5 100%)}
.brand{position:absolute;left:108px;top:60px;display:flex;align-items:center;gap:12px;font-size:30px;font-weight:500;letter-spacing:2px;color:var(--ink)}
.brand i{width:18px;height:18px;background:var(--blue);display:block}
.topbar{position:absolute;right:58px;top:14px;display:flex;align-items:center;gap:8px;font-size:16px;color:var(--white)}
.topbar .phone{display:flex;align-items:center;gap:6px;margin-right:10px}
.soc{width:30px;height:30px;border-radius:50%;border:1.5px solid var(--white)}
.nav{position:absolute;left:513px;top:63px;display:flex;gap:20px;font-size:15px;color:var(--white)}
.nav span:first-child{border-bottom:2px solid var(--white);padding-bottom:2px}
.hero h1{position:absolute;left:108px;top:236px;font-size:62px;font-weight:700;letter-spacing:1px}
.hero p{position:absolute;left:115px;top:318px;width:440px;font-size:14.5px;line-height:27px;color:#2a2f36}
.arrow{position:absolute;top:308px}
.dots{position:absolute;left:565px;top:558px;display:flex;gap:6px}
.dots b{width:11px;height:11px;border-radius:50%;background:rgba(255,255,255,.75)}
.dots b:first-child{background:var(--white)}

/* section heads */
.eyebrow{position:absolute;left:0;width:1200px;text-align:center;color:var(--blue);font-size:15px;font-weight:700;letter-spacing:.5px}
.heading{position:absolute;left:0;width:1200px;text-align:center;font-size:40px;font-weight:700}
.lead{position:absolute;left:0;width:1200px;text-align:center;font-size:15.5px;line-height:27px;color:#2d333b}

/* services */
.card{position:absolute;width:314px;height:440px;background:var(--card)}
.card .pic{height:206px;width:100%}
.card .icon{position:absolute;left:127px;top:172px;width:60px;height:60px;border-radius:50%;background:var(--white);display:flex;align-items:center;justify-content:center}
.card h3{position:absolute;top:240px;left:20px;right:20px;text-align:center;font-size:21px;line-height:28px;font-weight:700}
.card p{position:absolute;top:312px;left:14px;right:14px;text-align:center;font-size:13px;line-height:28.5px;color:var(--text)}

/* about */
.about-band{position:absolute;left:0;top:1836px;width:1200px;height:498px;background:var(--soft)}
.title{position:absolute;font-size:38px;font-weight:700}
.body{position:absolute;font-size:13px;line-height:27.5px;color:#3e4550}
.ghost{position:absolute;background:rgba(26,143,214,.05)}

/* partner */
.item{position:absolute;left:115px;width:460px}
.item .mark{position:absolute;left:0;top:2px;width:22px;height:22px;border-width:2.5px}
.item h4{margin-left:40px;font-size:19px;font-weight:700}
.item p{margin-left:40px;margin-top:8px;font-size:12.5px;line-height:25px;color:var(--text)}

/* blog */
.side{position:absolute;top:3292px;height:353px;background:var(--blue-dark);color:var(--white);overflow:hidden}
.side h5{font-size:20px;line-height:27px;font-weight:700}
.side p{margin-top:20px;font-size:12.5px;line-height:25.5px}
.feature{position:absolute;left:177px;top:3255px;width:845px;height:424px;box-shadow:0 10px 30px rgba(0,0,0,.15)}
.feature .panel{position:absolute;left:419px;top:0;width:426px;height:424px;background:linear-gradient(160deg,#2a9fe0,#1178c0);color:var(--white);padding:118px 40px 0 40px}
.feature h5{font-size:20px;line-height:27px;font-weight:700}
.feature p{margin-top:14px;font-size:12.5px;line-height:25.5px}

/* contact */
.contact-band{position:absolute;left:0;top:3809px;width:1200px;height:628px;background:var(--soft)}
.badge{position:absolute;left:388px;top:4145px;width:212px;height:212px;border-radius:50%;background:var(--blue-dark);border:5px solid var(--white);color:var(--white);text-align:center;padding-top:40px;box-shadow:0 6px 18px rgba(0,0,0,.2)}
.badge strong{display:block;font-size:38px;line-height:40px;font-weight:900}
.badge span{display:block;margin-top:6px;font-size:13px;font-weight:700;letter-spacing:1px}
.field{position:absolute;left:645px;width:414px;background:var(--white);border:1px solid var(--line);font-size:13px;color:#454b54;padding:16px 10px}

/* footer */
.footer{position:absolute;left:0;top:4437px;width:1200px;height:348px;background:var(--black);color:var(--white)}
.footer h6{position:absolute;top:78px;font-size:16px;font-weight:700}
.footer ul{position:absolute;top:110px;list-style:none;font-size:13px;line-height:26.5px}
.finput{position:absolute;height:34px;background:var(--white);color:#777;font-size:12px;padding:10px 8px}
.fbrand{position:absolute;left:918px;top:108px;display:flex;align-items:center;gap:10px;font-size:21px;letter-spacing:1.5px;font-weight:500}
.fbrand i{width:14px;height:14px;background:var(--white);display:block}
.fsoc{position:absolute;top:170px;width:31px;height:31px;border-radius:50%;background:var(--blue)}
.rule{position:absolute;left:113px;top:284px;width:995px;height:1px;background:#333}
.copy{position:absolute;left:0;top:310px;width:1200px;text-align:center;font-size:13px}
</style>
</head>
<body>

<!-- HERO -->
<header class="hero">
  <div class="photo" role="img" aria-label="Photo of a smiling business team walking through a bright office" style="left:560px;top:0;width:640px;height:607px;background:linear-gradient(90deg,rgba(230,235,240,0) 0%,rgba(120,135,145,.35) 60%,rgba(70,85,95,.45) 100%)"></div>
  <div class="brand"><i></i>BRIGHT HARBOR</div>
  <div class="topbar">
    <span class="phone">
      <svg width="14" height="14" viewBox="0 0 24 24"><path fill="#fff" d="M6.6 10.8a15.1 15.1 0 0 0 6.6 6.6l2.2-2.2a1 1 0 0 1 1-.25 11.4 11.4 0 0 0 3.6.6 1 1 0 0 1 1 1V20a1 1 0 0 1-1 1A17 17 0 0 1 3 4a1 1 0 0 1 1-1h3.5a1 1 0 0 1 1 1c0 1.25.2 2.45.6 3.6a1 1 0 0 1-.25 1z"/></svg>
      555 - 014 - 2290
    </span>
    <span class="soc"></span><span class="soc"></span><span class="soc"></span><span class="soc"></span>
  </div>
  <nav class="nav"><span>SERVICES</span><span>COMPANY</span><span>PARTNER SERVICES</span><span>SUPPORT</span><span>BLOG</span><span>CONTACT US</span></nav>
  <svg class="arrow" style="left:74px" width="14" height="26" viewBox="0 0 14 26"><path d="M12 2 2 13l10 11" fill="none" stroke="#333" stroke-width="1.6"/></svg>
  <svg class="arrow" style="left:1108px" width="14" height="26" viewBox="0 0 14 26"><path d="M2 2l10 11L2 24" fill="none" stroke="#fff" stroke-width="1.6"/></svg>
  <h1>BRIGHT HARBOR</h1>
  <p>Lorem ipsum dolor sit amet, consectetur cing elit, sed do eiusmod tempor incididunt ut labore et dolore magna aliqua.</p>
  <div class="btn" style="left:115px;top:392px;width:169px;height:48px">GET STARTED</div>
  <div class="dots"><b></b><b></b><b></b><b></b></div>
</header>

<!-- SERVICES -->
<section class="services">
  <div class="eyebrow" style="top:684px">OUR SERVICES</div>
  <h2 class="heading" style="top:705px">WHAT WE OFFER</h2>
  <div class="lead" style="top:758px">Lorem ipsum dolor sit amet, consectetur adipiscing elit, sed do eiusmod tempor</div>

  <article class="card" style="left:111px;top:812px"><div class="pic" role="img" aria-label="Hands holding a glowing cloud network graphic" style="background:linear-gradient(135deg,#3a3f46,#15181c)"></div><div class="icon"><svg width="30" height="30"><circle cx="15" cy="15" r="11" fill="none" stroke="#1a8fd6" stroke-width="2"/><circle cx="15" cy="15" r="4" fill="#1a8fd6"/></svg></div><h3>THE STANDARD LOREM IPSUM</h3><p>Lorem ipsum dolor sit amet, conur adipiscing elit, sed do eiusmd tempor incididunt ut labore et dolore magna qua. Quis ipsum suspendisse ultrices gravida. Risus commodo</p></article>
  <article class="card" style="left:442px;top:812px"><div class="pic" role="img" aria-label="Colleagues discussing plans at a whiteboard" style="background:linear-gradient(135deg,#dfe6ec,#8a99a8)"></div><div class="icon"><svg width="30" height="30"><rect x="5" y="7" width="20" height="14" fill="none" stroke="#1a8fd6" stroke-width="2"/><path d="M10 25h10" stroke="#1a8fd6" stroke-width="2"/></svg></div><h3>THE STANDARD LOREM IPSUM</h3><p>Lorem ipsum dolor sit amet, conur adipiscing elit, sed do eiusmd tempor incididunt ut labore et dolore magna qua. Quis ipsum suspendisse ultrices gravida. Risus commodo</p></article>
  <article class="card" style="left:775px;top:812px"><div class="pic" role="img" aria-label="Businessman touching a digital network interface" style="background:linear-gradient(135deg,#2c5b88,#0e2338)"></div><div class="icon"><svg width="30" height="30"><path d="M7 7l16 16M23 7 7 23" stroke="#1a8fd6" stroke-width="2.5"/></svg></div><h3>THE STANDARD LOREM IPSUM</h3><p>Lorem ipsum dolor sit amet, conur adipiscing elit, sed do eiusmd tempor incididunt ut labore et dolore magna qua. Quis ipsum suspendisse ultrices gravida. Risus commodo</p></article>

  <article class="card" style="left:111px;top:1271px"><div class="pic" role="img" aria-label="Team meeting around a conference table" style="background:linear-gradient(135deg,#e4e9ee,#7d8b98)"></div><div class="icon"><svg width="30" height="30"><rect x="9" y="4" width="12" height="8" fill="none" stroke="#1a8fd6" stroke-width="2"/><path d="M15 12v6M6 18h18M6 18v6M15 18v6M24 18v6" stroke="#1a8fd6" stroke-width="2" fill="none"/></svg></div><h3>THE STANDARD LOREM IPSUM</h3><p>Lorem ipsum dolor sit amet, conur adipiscing elit, sed do eiusmd tempor incididunt ut labore et dolore magna qua. Quis ipsum suspendisse ultrices gravida. Risus commodo</p></article>
  <article class="card" style="left:442px;top:1271px"><div class="pic" role="img" aria-label="Developer working at a desk with several monitors" style="background:linear-gradient(135deg,#c9d3dc,#4c5864)"></div><div class="icon"><svg width="30" height="30"><rect x="6" y="5" width="18" height="20" fill="none" stroke="#1a8fd6" stroke-width="2"/><path d="M10 11h10M10 15h10M10 19h6" stroke="#1a8fd6" stroke-width="2"/></svg></div><h3>THE STANDARD LOREM IPSUM</h3><p>Lorem ipsum dolor sit amet, conur adipiscing elit, sed do eiusmd tempor incididunt ut labore et dolore magna qua. Quis ipsum suspendisse ultrices gravida. Risus commodo</p></article>
  <article class="card" style="left:775px;top:1271px"><div class="pic" role="img" aria-label="Man viewing holographic data screens" style="background:linear-gradient(135deg,#3d6c96,#0d1e2f)"></div><div class="icon"><svg width="30" height="30"><path d="M8 21a6 6 0 0 1 1-12 7 7 0 0 1 13 2 5 5 0 0 1 0 10z" fill="none" stroke="#1a8fd6" stroke-width="2"/></svg></div><h3>THE STANDARD LOREM IPSUM</h3><p>Lorem ipsum dolor sit amet, conur adipiscing elit, sed do eiusmd tempor incididunt ut labore et dolore magna qua. Quis ipsum suspendisse ultrices gravida. Risus commodo</p></article>
</section>

<!-- ABOUT -->
<section class="about">
  <div class="about-band"></div>
  <div class="ghost" style="left:935px;top:2150px;width:160px;height:184px"></div>
  <div class="photo" role="img" aria-label="Smiling colleagues working together at a computer" style="left:108px;top:1802px;width:453px;height:574px;background:linear-gradient(135deg,#d8dadb,#a98a6a 55%,#4a3a2c);box-shadow:0 10px 30px rgba(0,0,0,.15)"></div>
  <span class="mark abs" style="left:638px;top:1880px"></span>
  <h2 class="title" style="left:635px;top:1940px">ABOUT US</h2>
  <p class="body" style="left:635px;top:1998px;width:455px">Sed ut perspiciatis unde omnis iste natus error sit m accusantium doloremque laudantium, totam rem aperiam, eaque io inventore veritatis et quasi architecto beatae vitae dicta sunt explicabo. Nemo enim ipsam voluptatem quia voluptas sit aspernatur aut odit aut fugit, sed quia consequuntur magni dolores eos qui ratione voluptatem sequi nesciunt. Neque porro quisquam est</p>
  <p class="body" style="left:635px;top:2146px;width:455px">Ut enim ad minima veniam, quis nostrum exercitationem ulm corporis suscipit laboriosam, nisi ut aliquid ex ea commodi consequatur</p>
  <div class="btn" style="left:635px;top:2222px;width:169px;height:52px">LEARN MORE</div>
</section>

<!-- PARTNER SERVICES -->
<section class="partner">
  <span class="mark abs" style="left:118px;top:2432px"></span>
  <h2 class="title" style="left:115px;top:2482px;font-size:36px">PARTNER SERVICES</h2>
  <div class="item" style="top:2546px"><span class="mark"></span><h4>PRE-SALES</h4><p>Sed ut perspiciatis unde omnis iste natus error sit voluatem accusantium doloremque laudantium, totam rem aperiam, eaque ipsa quae ab illo inventore veritatis et quasi architecto beatae</p></div>
  <div class="item" style="top:2663px"><span class="mark"></span><h4>APPLICATION CONSULTING SERVICES</h4><p>Sed ut perspiciatis unde omnis iste natus error sit voluatem accusantium doloremque laudantium, totam rem aperiam, eaque ipsa quae ab illo inventore veritatis et quasi architecto beatae</p></div>
  <div class="item" style="top:2780px"><span class="mark"></span><h4>MANAGED SERVICES</h4><p>Sed ut perspiciatis unde omnis iste natus error sit voluatem accusantium doloremque laudantium, totam rem aperiam, eaque ipsa quae ab illo inventore veritatis et quasi architecto beatae</p></div>
  <div class="item" style="top:2897px"><span class="mark"></span><h4>EDUCATION &amp; TRAINING</h4><p>Sed ut perspiciatis unde omnis iste natus error sit voluatem accusantium doloremque laudantium, totam rem aperiam, eaque ipsa quae ab illo inventore veritatis et quasi architecto beatae</p></div>
  <div class="photo" role="img" aria-label="Young team gathered around a laptop in a dim office" style="left:635px;top:2400px;width:454px;height:591px;background:linear-gradient(150deg,#3e4a4f,#6b6a5e 50%,#20262a);box-shadow:0 10px 30px rgba(0,0,0,.15)"></div>
</section>

<!-- BLOG -->
<section class="blog">
  <div class="eyebrow" style="top:3096px">UPDATES</div>
  <h2 class="heading" style="top:3118px">LATEST BLOG</h2>
  <div class="lead" style="top:3170px;width:660px;left:270px">Lorem ipsum dolor sit amet, consectetur adipiscing elit, sed do eiusmod tempor incididunt ut labore et dolore magna aliqua. Quis ipsum suspendisse ultrices gravida.</div>

  <div class="side" style="left:0;width:156px;padding:80px 0 0 0"><div style="margin-left:-130px;width:270px"><h5>Ipsum passage,</h5><p>Lorem ipsum dolor adipiscing elit, sed do dolore magna aliqua. Quis modo viverra maecenas sit amet, consectetur incidunt ut labore et dolore gravida. Risus commodo facilisis.</p></div></div>
  <div class="side" style="left:1044px;width:156px;padding:80px 0 0 40px"><div style="width:270px"><h5>The standard Lorem used since the 1500s</h5><p>Lorem ipsum dolor sit amet eiusmod tempor incididunt ipsum suspendisse ultrices accumsan lacus vel facilisis adipiscing elit, sed do eiusmod magna aliqua. Quis ipsum viverra maecenas accumsan</p></div></div>

  <article class="feature">
    <div class="photo" role="img" aria-label="Woman thinking in front of a computer screen" style="left:0;top:0;width:419px;height:424px;background:linear-gradient(135deg,#cfd2cc,#8a7c6a 60%,#3c352d)"></div>
    <div class="panel">
      <h5>The standard Lorem Ipsum passage, used since the 1500s</h5>
      <p>Lorem ipsum dolor sit amet, consectetur adipiscing elit, sed do eiusmod tempor incididunt ut labore et dolore magna aliqua. Quis ipsum suspendisse ultrices gravida. Risudo viverra maecenas accumsan lacus vel facilisis. Lorem dolor sit amet, consectetur adipiscing elit, sed do eiusmod tor incididunt ut labore et dolore magna aliqua. Quis ipsndisse ultrices gravida. Risus commodo viverra maecenas accumsan lacus vel facilisis.</p>
    </div>
  </article>
</section>

<!-- CONTACT -->
<section class="contact">
  <div class="contact-band"></div>
  <div class="ghost" style="left:940px;top:4120px;width:220px;height:317px"></div>
  <div class="photo" role="img" aria-label="Modern glass office tower against a cloudy sky" style="left:117px;top:3764px;width:453px;height:558px;background:linear-gradient(180deg,#c9ccc9,#7d817f 55%,#2f3230)"></div>
  <div class="badge"><strong>WORK<br>WITH<br>US</strong><span>CONTACT US</span></div>
  <h2 class="title" style="left:645px;top:3860px;line-height:42px">CONTACT US WITH<br>ANY QUESTIONS</h2>
  <p class="body" style="left:645px;top:3942px;width:430px;font-size:13px;line-height:27px">Lorem ipsum dolor sit amet, consectetur adipiscing elit, sed do eiusmod tempor incididunt ut labore et dolore magna aliqua.</p>
  <div class="field" style="top:4000px;height:50px">First Name</div>
  <div class="field" style="top:4061px;height:51px">Company Name</div>
  <div class="field" style="top:4121px;height:50px">Enter Email</div>
  <div class="field" style="top:4182px;height:115px">Message</div>
  <div class="btn" style="left:645px;top:4325px;width:169px;height:51px">SUBMIT</div>
</section>

<!-- FOOTER -->
<footer class="footer">
  <h6 style="left:113px">GET INSIGHTS &amp; UPDATES</h6>
  <div class="finput" style="left:113px;top:107px;width:160px">Name</div>
  <div class="finput" style="left:282px;top:107px;width:160px">Phone</div>
  <div class="finput" style="left:113px;top:152px;width:329px">Enter Email</div>
  <div class="abs" style="left:113px;top:197px;width:329px;height:41px;background:var(--blue);display:flex;align-items:center;justify-content:center;font-weight:700;font-size:15px">SUBSCRIBE</div>

  <h6 style="left:509px">QUICK LINKS</h6>
  <ul style="left:509px"><li>- Home</li><li>- Company</li><li>- Services</li><li>- Partner services</li><li>- Support</li><li>- Blog</li><li>- Contact Us</li></ul>

  <h6 style="left:682px">HELPFUL INFORMATION</h6>
  <ul style="left:682px"><li>- Legal</li><li>- Data protection</li><li>- Declaration</li><li>- Terms &amp; Conditions</li><li>- Sitemap</li></ul>

  <div class="fbrand"><i></i>BRIGHT HARBOR</div>
  <span class="fsoc" style="left:926px"></span>
  <span class="fsoc" style="left:970px"></span>
  <span class="fsoc" style="left:1014px"></span>
  <span class="fsoc" style="left:1058px"></span>

  <div class="rule"></div>
  <div class="copy">© 2021 Bright Harbor. All Rights Reserved.</div>
</footer>

</body>
</html>
```